Halvorsen Construction Needs a Business Card

Our current business card is very bland, and since we have a new logo, we would like a new business card design to reflect our company. It can be a single-sided or two-sided card, but it is important that our contact information appears on the same side. I am attaching a copy of our old card and our new logo. If you need the logo in another format than the one I'm sending, please let me know. This is the information that we must have on our card, but not necessarily in any specific order:
1) Our logo
2) General Contractor
3) Dale Halvorsen, Owner
4) 482 Commerce Ridge Road, Cedar Flats, Westmark 35871
5) Office: 555-555-0147
7) Fax: 555-555-0148
8) Cell: 555-555-0193
9) halvorsenconstruction@qvl-mail.net
10) halvorsenconstruction-example.com (can be omitted if necessary)
Also, I will need files in a format that I can alter if any of the above information changes in the near future. Thank you in advance for your submissions!
Target Market(s)
Commercial and residential clients, architects, and subcontractors.
Industry/Entity Type
Business
Look and feel

```html
<!DOCTYPE html>
<html lang="en">
<head>
<meta charset="utf-8">
<title>Halvorsen Construction Business Card</title>
<link rel="stylesheet" href="https://fonts.googleapis.com/css2?family=Arimo:wght@400;700&display=swap">
<style>
  :root {
    --stage: #1c1c1c;
    --card-dark: #2a2627;
    --card-light: #ffffff;
    --gold: #f5c431;
    --ink: #231f20;
    --soft-grey: #e6e6e7;
    --text-light: #f2f2f2;
  }
  * { box-sizing: border-box; margin: 0; padding: 0; }
  html, body { width: 1200px; height: 900px; overflow: hidden; }
  body {
    background: var(--stage);
    font-family: "Arimo", Arial, sans-serif;
    position: relative;
  }
  .card {
    position: absolute;
    left: 337px;
    width: 525px;
    height: 300px;
    overflow: hidden;
    box-shadow: 0 10px 30px rgba(0,0,0,.5);
  }
  /* Back of card */
  .card-back { top: 100px; background: var(--card-dark); }
  .card-back .gold-band {
    position: absolute; left: 0; right: 0; bottom: 0; height: 14px;
    background: var(--gold);
  }
  .card-back .brand-mark {
    position: absolute; left: 0; right: 0; top: 118px;
    display: flex; align-items: center; justify-content: center; gap: 12px;
  }
  .brand-mark .mark-square { width: 30px; height: 30px; background: var(--gold); }
  .brand-mark .mark-name {
    color: var(--gold); font-weight: 700; font-size: 26px; letter-spacing: 1px;
    text-transform: uppercase;
  }
  /* Front of card */
  .card-front { top: 500px; background: var(--card-dark); }
  .front-top {
    position: absolute; left: 0; top: 0; width: 100%; height: 158px;
    background: var(--card-light);
  }
  .front-top .faint-square {
    position: absolute; right: 22px; top: 16px; width: 118px; height: 118px;
    background: var(--soft-grey);
  }
  .gold-rule {
    position: absolute; left: 0; top: 158px; width: 100%; height: 6px;
    background: var(--gold);
  }
  .logo-lockup {
    position: absolute; left: 26px; top: 66px;
    display: flex; align-items: center; gap: 9px;
  }
  .logo-lockup .lockup-square { width: 34px; height: 34px; background: var(--ink); }
  .logo-lockup .lockup-name {
    color: var(--ink); font-weight: 700; font-size: 19px; line-height: 1.05;
    text-transform: uppercase; letter-spacing: .5px;
  }
  .tagline {
    position: absolute; left: 258px; top: 118px;
    color: var(--ink); font-weight: 700; font-size: 12px;
  }
  .person { position: absolute; left: 32px; top: 184px; color: var(--text-light); }
  .person .name { color: var(--gold); font-weight: 700; font-size: 19px; }
  .person .role { font-size: 11px; margin-top: 1px; }
  .person .address { font-size: 11.5px; line-height: 1.45; margin-top: 14px; }
  .divider {
    position: absolute; left: 268px; top: 176px; width: 1px; height: 92px;
    background: var(--gold); opacity: .6;
  }
  .contact {
    position: absolute; left: 282px; top: 180px; list-style: none;
    color: var(--text-light); font-size: 11px; line-height: 1.5;
  }
  .contact .label { color: var(--gold); font-weight: 700; margin-right: 3px; }
</style>
</head>
<body>
  <section class="card card-back" aria-label="Business card back">
    <div class="brand-mark">
      <span class="mark-square"></span>
      <span class="mark-name">Halvorsen Construction</span>
    </div>
    <div class="gold-band"></div>
  </section>

  <section class="card card-front" aria-label="Business card front">
    <div class="front-top">
      <div class="faint-square"></div>
    </div>
    <div class="logo-lockup">
      <span class="lockup-square"></span>
      <span class="lockup-name">Halvorsen<br>Construction</span>
    </div>
    <p class="tagline">General Contractor</p>
    <div class="gold-rule"></div>

    <div class="person">
      <p class="name">Dale Halvorsen</p>
      <p class="role">Owner</p>
      <p class="address">482 Commerce Ridge Road,<br>Cedar Flats, Westmark 35871</p>
    </div>

    <div class="divider"></div>

    <ul class="contact">
      <li><span class="label">Office</span>555-555-0147</li>
      <li><span class="label">Fax</span>555-555-0148</li>
      <li><span class="label">Cell</span>555-555-0193</li>
      <li>halvorsenconstruction@qvl-mail.net</li>
      <li>www.halvorsenconstruction-example.com</li>
    </ul>
  </section>
</body>
</html>
```